Tallow & Mersey Needs New Stationery / Letterhead Design

We need new stationery to match our new logo (attached). Tallow & Mersey is a 34 year old nationwide law firm located in Houston Tx. They do personal injury law and pharmaceutical litigation.

WE DO NOT NEED BUSINESS CARDS.

Attached are several different file formats of the new logo.

Reason: We will make a decision in the next couple days. Finalizing edits now. Thank you!

Target Market(s)

consumers who have been injured due to the negligence of another or by a pharmaceutical drug or defective medical device. Also co-counsel and opposing counsel (law firms0.

Industry/Entity Type

Law Firm

Requirements
Must have
• logo
• Tallow & Mersey, LLP
• 7183 Corvid Lane, Suite 1000
• Brenford, TX 75591
• Tel: (555) 408-1936
• Fax: (555) 408-2275
• www.tallowandmersey.example
• Must have colors in the logo.
• Make the font go with the logo - not necessarily the same, but something that goes well with it.

```html
<!DOCTYPE html>
<html lang="en">
<head>
<meta charset="utf-8">
<title>Tallow &amp; Mersey Stationery</title>
<link rel="stylesheet" href="https://fonts.googleapis.com/css2?family=Montserrat:wght@300;400;500;600;700&display=swap">
<style>
  :root {
    --navy: #1b3a63;
    --ink: #3a3a3a;
    --muted: #555b66;
    --paper: #ffffff;
    --paper-end: #f1f1f2;
    --backdrop: #e8e6e3;
    --rule: #1b3a63;
  }
  * { margin: 0; padding: 0; box-sizing: border-box; }
  html, body { width: 1200px; height: 735px; overflow: hidden; }
  body {
    background: var(--backdrop);
    font-family: "Montserrat", sans-serif;
    color: var(--ink);
    position: relative;
  }

  /* Letterhead */
  .letterhead {
    position: absolute; left: 56px; top: 21px; width: 521px; height: 678px;
    background: linear-gradient(180deg, var(--paper) 0%, var(--paper-end) 100%);
    box-shadow: 0 2px 6px rgba(0,0,0,.18);
  }
  .brand { position: absolute; display: flex; flex-direction: column; }
  .brand-line { display: flex; align-items: center; gap: 6px; }
  .brand-mark { width: 12px; height: 12px; background: var(--navy); }
  .brand-name {
    font-weight: 600; color: var(--navy); font-size: 15.5px; letter-spacing: .3px; white-space: nowrap;
  }
  .brand-tag {
    font-size: 5.6px; letter-spacing: 1.2px; color: var(--ink); text-transform: uppercase; margin-top: 3px;
  }
  .letterhead .brand { left: 34px; top: 48px; }
  .divider { position: absolute; top: 63px; width: 1px; height: 18px; background: var(--rule); }
  .contact {
    position: absolute; top: 64px; display: flex; gap: 4px; font-size: 6.4px; line-height: 8px; color: #222;
  }
  .contact svg { flex: none; margin-top: 1px; }
  .contact-lines { display: flex; flex-direction: column; }
  .phone-row { display: flex; align-items: center; gap: 4px; }

  .letter-body {
    position: absolute; left: 35px; top: 155px; width: 452px;
    font-size: 9.1px; line-height: 12.8px; font-weight: 300; color: var(--ink);
  }
  .letter-body p { text-align: justify; margin-bottom: 12.8px; }
  .letter-body .salutation { margin-bottom: 12.6px; }
  .letter-body .spaced { margin-top: 2px; }
  .signature {
    width: 66px; height: 52px; margin: 12px 0 14px;
    background: linear-gradient(135deg, rgba(40,40,40,.0) 0%, rgba(40,40,40,.18) 50%, rgba(40,40,40,.0) 100%);
  }
  .signer { line-height: 12.8px; }
  .site {
    font-size: 6.2px; font-weight: 700; letter-spacing: 1.1px; color: var(--navy);
  }
  .letterhead .site { position: absolute; left: 0; right: 0; top: 652px; text-align: center; }

  /* Envelope front */
  .envelope-front {
    position: absolute; left: 604px; top: 89px; width: 546px; height: 240px;
    background: var(--paper); box-shadow: 0 2px 6px rgba(0,0,0,.18);
  }
  .envelope-front .brand { left: 28px; top: 56px; }
  .envelope-front .brand-name { font-size: 13px; }
  .envelope-front .brand-mark { width: 10px; height: 10px; }
  .envelope-front .brand-tag { font-size: 4.7px; }
  .envelope-front .contact { left: 29px; top: 208px; font-size: 6.4px; align-items: center; }
  .envelope-front .site { position: absolute; right: 30px; top: 209px; }

  /* Envelope back */
  .envelope-back {
    position: absolute; left: 604px; top: 353px; width: 546px; height: 240px;
    background: var(--paper); box-shadow: 0 2px 6px rgba(0,0,0,.18);
  }
  .envelope-back svg.flap { position: absolute; left: 0; top: 0; }
  .flap-name {
    position: absolute; left: 0; right: 0; top: 31px; text-align: center;
    color: #fff; font-weight: 600; font-size: 15px; letter-spacing: .3px;
  }
</style>
</head>
<body>

<section class="letterhead">
  <div class="brand">
    <div class="brand-line"><span class="brand-mark"></span><span class="brand-name">Tallow &amp; Mersey</span></div>
    <span class="brand-tag">Attorneys at Law / Founded in 1984</span>
  </div>
  <span class="divider" style="left:218px"></span>
  <div class="contact" style="left:258px">
    <svg width="6" height="8" viewBox="0 0 6 8"><path d="M3 0a3 3 0 0 1 3 3c0 2-3 5-3 5S0 5 0 3a3 3 0 0 1 3-3z" fill="var(--navy)"/><circle cx="3" cy="3" r="1.1" fill="#fff"/></svg>
    <div class="contact-lines"><span>7183 Corvid Lane, Suite 1000</span><span>Brenford, TX 75591</span></div>
  </div>
  <span class="divider" style="left:388px"></span>
  <div class="contact" style="left:426px">
    <div class="contact-lines">
      <span class="phone-row"><svg width="7" height="7" viewBox="0 0 7 7"><path d="M1.4 0.3l1.2 1.5-.6 1a4 4 0 0 0 2 2l1-.6 1.5 1.2-.7 1.3C3.3 6.7.3 3.7.1 1z" fill="var(--navy)"/></svg>(555) 408-1936</span>
      <span class="phone-row"><svg width="7" height="7" viewBox="0 0 7 7"><rect x="0.5" y="3" width="6" height="3.5" rx=".6" fill="var(--navy)"/><rect x="1.7" y="0.5" width="3.6" height="2.8" fill="var(--navy)"/></svg>(555) 408-2275</span>
    </div>
  </div>

  <div class="letter-body">
    <p class="salutation">Dear customer,</p>
    <p>Lorem ipsum dolor sit amet, consectetur adipisicing elit, sed do eiusmod tempor incididunt ut labore et dolore magna aliqua. Ut enim ad minim veniam, quis nostrud exercitation ullamco laboris nisi ut aliquip ex ea commodo consequat. Duis aute irure dolor in reprehenderit in voluptate velit esse cillum dolore eu fugiat nulla pariatur. Excepteur sint occaecat cupidatat non proident, sunt in culpa qui officia deserunt mollit anim id est laborum.</p>
    <p>Lorem ipsum dolor sit amet, consectetur adipisicing elit, sed do eiusmod tempor incididunt ut labore et dolore magna aliqua. Ut enim ad minim veniam, quis nostrud exercitation ullamco laboris nisi ut aliquip ex ea commodo consequat. Duis aute irure dolor in reprehenderit in voluptate velit esse cillum dolore eu fugiat nulla pariatur. Excepteur sint occaecat cupidatat non proident, sunt in culpa qui officia deserunt mollit anim id est laborum.</p>
    <p class="spaced">Lorem ipsum dolor sit amet, consectetur adipisicing elit, sed do eiusmod tempor incididunt ut labore et dolore magna aliqua. Ut enim ad minim veniam, quis nostrud exercitation ullamco laboris nisi ut aliquip ex ea commodo consequat. Duis aute irure dolor in reprehenderit in voluptate velit esse cillum dolore eu fugiat nulla pariatur. Excepteur sint occaecat cupidatat non proident, sunt in culpa qui officia deserunt mollit anim id est laborum.</p>
    <p class="closing">Yours Sincerely,</p>
    <div class="signature" role="img" aria-label="Handwritten signature of Marcus Hale"></div>
    <div class="signer">Marcus Hale<br>General Director</div>
  </div>

  <div class="site">www.tallowandmersey.example</div>
</section>

<section class="envelope-front">
  <div class="brand">
    <div class="brand-line"><span class="brand-mark"></span><span class="brand-name">Tallow &amp; Mersey</span></div>
    <span class="brand-tag">Attorneys at Law / Founded in 1984</span>
  </div>
  <div class="contact">
    <svg width="6" height="8" viewBox="0 0 6 8"><path d="M3 0a3 3 0 0 1 3 3c0 2-3 5-3 5S0 5 0 3a3 3 0 0 1 3-3z" fill="var(--navy)"/><circle cx="3" cy="3" r="1.1" fill="#fff"/></svg>
    <span>7183 Corvid Lane, Suite 1000, Brenford, TX 75591</span>
  </div>
  <div class="site">www.tallowandmersey.example</div>
</section>

<section class="envelope-back">
  <svg class="flap" width="546" height="240" viewBox="0 0 546 240">
    <path d="M0 0H546C542 14 538 32 516 39L300 79Q273 85 246 79L30 39C8 32 4 14 0 0Z" fill="var(--navy)"/>
  </svg>
  <div class="flap-name">Tallow &amp; Mersey</div>
</section>

</body>
</html>
```